Web Design For Metal Recycling Company

We are a scrap and recycling company dealing mainly in scrap metal base in Singapore. We deal in both domestic market and international market. Currently we are still unsure if we want to have a "lively" or "professional" company image so we will leave it to the designer to deem what is good.

We wish for a website to be able to "Retain" the interest of new visitor and at the same time able to give enough information for new and existing customer. We would also wish for design that will get the visitor to "Engage" us.

The attached is the logo for the company and we would want to incorporate that into the website. Either of the logo is fine.

```html
<!DOCTYPE html>
<html lang="en">
<head>
<meta charset="utf-8">
<title>Lim Teck Hong Recycling</title>
<link rel="stylesheet" href="https://fonts.googleapis.com/css2?family=Archivo+Black&family=Didact+Gothic&family=Federo&family=Questrial&display=swap">
<style>
:root{
  --navy:#1f3b55;
  --navy-top:#355674;
  --ink:#13222f;
  --footer:#1d2d3c;
  --gold:#c99a1f;
  --grey-band:#d9d9d9;
  --paper:#f0f0f0;
  --services:#a3a3a3;
  --text:#6d6d6d;
  --dark-text:#333;
  --accent:#cf5a12;
  --label:#1a3149;
  --white:#fff;
}
*{margin:0;padding:0;box-sizing:border-box}
html,body{width:1185px;height:1200px;overflow:hidden}
body{position:relative;background:var(--grey-band);font-family:"Didact Gothic",sans-serif;color:var(--dark-text)}
.abs{position:absolute}

.site-header{left:0;top:0;width:1185px;height:90px;background:linear-gradient(var(--navy-top),var(--navy))}
.brand{left:152px;top:21px;display:flex;align-items:center;gap:10px}
.brand-mark{width:56px;height:56px;border:3px solid var(--gold)}
.brand-name{font-family:"Questrial",sans-serif;font-size:25px;color:var(--gold);letter-spacing:1px}
.social{right:153px;top:14px;display:flex;gap:5px}
.social span{width:24px;height:24px;border-radius:50%;background:var(--ink)}
.nav{right:152px;top:59px;display:flex;gap:26px;font-family:"Questrial",sans-serif;font-size:13px;color:#dfe6ec}

.hero-band{left:0;top:90px;width:1185px;height:378px;background:var(--ink)}
.hero-photo{left:135px;top:90px;width:913px;height:378px;
  background:linear-gradient(90deg,#c7c9cc 0%,#8e9195 30%,#9a9ca0 37.5%,#b4522a 38%,#d17a48 52%,#8a3a1a 61%,#c9a53d 62%,#e0c76a 78%,#7a5a17 100%)}
.hero-title{left:135px;top:230px;width:913px;text-align:center;font-family:"Archivo Black",sans-serif;font-size:52px;color:var(--white);text-shadow:3px 3px 4px rgba(0,0,0,.55)}

.category{top:415px;width:182px;height:187px;background:var(--white);padding:3px}
.category .thumb{width:176px;height:150px}
.category .label{display:flex;justify-content:space-between;align-items:center;height:32px;padding:0 6px;font-family:"Questrial",sans-serif;font-size:17px;color:var(--label)}
.category .label svg{width:8px;height:8px}

.welcome{left:0;top:612px;width:1185px;height:207px;background:var(--paper)}
.welcome h1{position:absolute;top:24px;width:100%;text-align:center;font-family:"Federo",sans-serif;font-weight:400;font-size:29px;color:#666}
.welcome p{position:absolute;left:155px;top:73px;width:875px;text-align:center;font-size:14.6px;line-height:24px;color:var(--text)}
.tab-btn{left:477px;top:784px;width:233px;height:45px}
.tab-btn span{position:absolute;left:0;top:10px;width:100%;text-align:center;font-size:16px;color:#b9c0c6}

.services{left:0;top:819px;width:1185px;height:319px;background:var(--services)}
.services h2{position:absolute;top:44px;width:100%;text-align:center;font-family:"Archivo Black",sans-serif;font-weight:400;font-size:20px;color:var(--white);letter-spacing:1px}
.service-card{top:911px;width:405px;height:187px;background:var(--white);border-radius:6px;padding:10px 26px}
.service-card h3{font-family:"Questrial",sans-serif;font-weight:400;font-size:16px;color:var(--accent);margin-bottom:8px}
.service-card p{font-size:11px;line-height:15.4px;color:var(--dark-text);margin-bottom:15px;width:345px}
.card-btn{position:absolute;bottom:0;right:32px;width:100px;height:27px}
.card-btn span{position:absolute;left:0;top:6px;width:100%;text-align:center;font-size:12.5px;color:#b9c0c6}
.binder{left:564px;top:920px;width:58px;height:170px}

.site-footer{left:0;top:1138px;width:1185px;height:62px;background:var(--footer)}
.site-footer p{position:absolute;left:156px;top:22px;font-size:13px;color:#e4e8ec}
.footer-brand{right:67px;top:18px;display:flex;align-items:center;gap:6px}
.footer-brand i{width:30px;height:30px;border:2px solid #56606a}
.footer-brand span{font-family:"Questrial",sans-serif;font-size:15px;color:#56606a}
</style>
</head>
<body>
<header class="site-header abs">
  <div class="brand abs"><span class="brand-mark"></span><span class="brand-name">LIM TECK HONG</span></div>
  <div class="social abs"><span></span><span></span><span></span></div>
  <nav class="nav abs"><span>Home</span><span>About Us</span><span>Our Products</span><span>Our Services</span><span>Contact Us</span></nav>
</header>

<div class="hero-band abs"></div>
<div class="hero-photo abs" role="img" aria-label="Stacked aluminium profiles, copper wire and brass rods"></div>
<div class="hero-title abs">Scrap Metal Recyclers</div>

<div class="category abs" style="left:186px"><div class="thumb" role="img" aria-label="Pile of ferrous scrap steel" style="background:linear-gradient(#9fbfe0,#7a6a5a 45%,#5a4a3e)"></div><div class="label">Ferrous<svg viewBox="0 0 8 8"><path d="M0 2h4V0l4 4-4 4V6H0z" fill="#d21"/></svg></div></div>
<div class="category abs" style="left:394px"><div class="thumb" role="img" aria-label="Tangle of copper wire" style="background:linear-gradient(135deg,#c0562a,#e08a5a,#8a3416)"></div><div class="label">Non-Ferrous<svg viewBox="0 0 8 8"><path d="M0 2h4V0l4 4-4 4V6H0z" fill="#d21"/></svg></div></div>
<div class="category abs" style="left:604px"><div class="thumb" role="img" aria-label="Heap of electronic chips" style="background:linear-gradient(135deg,#555,#111 60%,#3a3a3a)"></div><div class="label">Electronic<svg viewBox="0 0 8 8"><path d="M0 2h4V0l4 4-4 4V6H0z" fill="#d21"/></svg></div></div>
<div class="category abs" style="left:817px"><div class="thumb" role="img" aria-label="Industrial machinery inside a plant" style="background:linear-gradient(#5a5a5e,#3a3a3e 60%,#7a7060)"></div><div class="label">Machinery<svg viewBox="0 0 8 8"><path d="M0 2h4V0l4 4-4 4V6H0z" fill="#d21"/></svg></div></div>

<section class="welcome abs">
  <h1>Welcome To !</h1>
  <p>Lim Teck Hong Hardware provides a one stop solution for procurement, recycling and trading of ferrous and non-ferrous scrap metal products for industries and individual. Lim Teck Hong Hardware was first established in 1981 as “Lim Teck Hong Lead Dealer” to provide the service of recycling of ferrous and non-ferrous scrap metal for the local market.</p>
</section>
<div class="tab-btn abs">
  <svg width="233" height="45" viewBox="0 0 233 45"><path d="M0 37h12v8z" fill="#5b6d7d"/><path d="M233 37h-12v8z" fill="#5b6d7d"/><path d="M20 0h193l10 37-2 8H12l-2-8z" fill="var(--ink)"/></svg>
  <span>Know more</span>
</div>

<section class="services abs"><h2>OUR SERVICES</h2></section>
<article class="service-card abs" style="left:180px">
  <h3>For Company</h3>
  <p>Our company provides on the spot weighing with our accurately calibrated and well maintained crane scale. Payment can be arrange to be made upon collection.</p>
  <p>Should your company scrap contain confidential information, our company will be more than welcome to have you at our scrap yard to witness your material being completely destroyed or sent you a photographic image as proof.</p>
  <div class="card-btn"><svg width="100" height="27" viewBox="0 0 100 27"><path d="M8 0h84l8 27H0z" fill="var(--ink)"/></svg><span>Know more</span></div>
</article>
<article class="service-card abs" style="left:601px">
  <h3>For Industrial</h3>
  <p>To serve our individual customer better, we are open daily (excluding public holiday) for you to bring your scrap material to our scrap yard for sale.</p>
  <p>At our yard, our friendly staff will assist you in separating your scrap material into different grade so as to ensure you get the most value out of your recyclable material.</p>
  <div class="card-btn"><svg width="100" height="27" viewBox="0 0 100 27"><path d="M8 0h84l8 27H0z" fill="var(--ink)"/></svg><span>Know more</span></div>
</article>
<svg class="binder abs" viewBox="0 0 58 170">
  <line x1="29" y1="8" x2="29" y2="162" stroke="#8e8e8e" stroke-width="3"/>
  <path d="M4 8q25-8 50 0q-25 8-50 0z" fill="none" stroke="#9a9a9a" stroke-width="4"/>
  <path d="M4 162q25-8 50 0q-25 8-50 0z" fill="none" stroke="#9a9a9a" stroke-width="4"/>
</svg>

<footer class="site-footer abs">
  <p>© Copyright 2014 Lim Teck Hong. All rights reserved.</p>
  <div class="footer-brand abs"><i></i><span>LIM TECK HONG</span></div>
</footer>
</body>
</html>
```